Real estate company needs a card that makes you say WOW!

We need an awesome business card for our real estate company, Stonebrook Realty Partners of Chicago, that will stand out from the crowd. We specialize in buying and selling real estate, property management, and real estate investments (Flips & Rentals). On the business card, I need the following:

- Our logo
- Services
- My name & contact info (Derek Ollanby, 630-517-2946, Derek@StonebrookRPC.com)
- My title (Director of Acquisitions)
- StonebrookRPC.com

I attached an EPS file of our logo. Let me know if you have any questions. Thank you in advance!

```html
<!DOCTYPE html>
<html lang="en">
<head>
<meta charset="utf-8">
<title>Stonebrook Realty Partners of Chicago – Business Card</title>
<link rel="stylesheet" href="https://fonts.googleapis.com/css2?family=Cinzel:wght@400;500&family=Caladea&display=swap">
<style>
  :root {
    --stage: #2c2c2c;
    --paper: #ffffff;
    --brand-blue: #1d5fa3;
    --sky-light: #2aa8e4;
    --sky-mid: #1f84cc;
    --sky-deep: #1a5b98;
    --skyline-light: #cfe7f7;
    --text-light: #ffffff;
  }
  * { box-sizing: border-box; margin: 0; padding: 0; }
  html, body {
    width: 1200px; height: 1000px; overflow: hidden;
    background: var(--stage);
  }
  .canvas { position: relative; width: 1200px; height: 1000px; }

  .card {
    position: absolute;
    width: 424px; height: 722px;
    overflow: hidden;
    box-shadow: 0 8px 24px rgba(0,0,0,.45);
  }
  .card--front { left: 121px; top: 128px; background: var(--paper); }
  .card--back {
    left: 677px; top: 118px;
    background: linear-gradient(180deg, var(--sky-light) 0%, var(--sky-mid) 45%, var(--sky-deep) 100%);
  }

  /* Front */
  .brand {
    position: absolute; left: 0; right: 0; top: 128px;
    text-align: center;
    font-family: "Caladea", Georgia, serif;
    color: var(--brand-blue);
  }
  .brand__name {
    font-size: 30px; letter-spacing: 1.5px; line-height: 1.15; text-transform: uppercase;
  }
  .brand__name span { display: block; font-size: 16px; letter-spacing: 1px; }
  .brand__mark {
    display: block; width: 14px; height: 14px; margin: 0 auto 12px;
    border-radius: 50%; background: var(--brand-blue);
  }

  .skyline {
    position: absolute; left: 0; right: 0;
  }
  .skyline--front {
    top: 265px; height: 97px;
    background: linear-gradient(180deg, var(--paper) 0%, var(--skyline-light) 35%, var(--sky-light) 100%);
  }
  .front__panel {
    position: absolute; left: 0; right: 0; top: 362px; bottom: 0;
    background: linear-gradient(180deg, var(--sky-light) 0%, var(--sky-mid) 45%, var(--sky-deep) 100%);
    color: var(--text-light);
    text-align: center;
  }
  .person__name {
    margin-top: 88px;
    font-family: "Cinzel", "Times New Roman", serif;
    font-weight: 500; font-size: 31px; letter-spacing: .5px;
  }
  .person__title {
    margin-top: 2px;
    font-family: "Caladea", Georgia, serif; font-size: 23px;
  }
  .contact {
    list-style: none; margin-top: 46px;
    font-family: "Caladea", Georgia, serif; font-size: 23px; line-height: 33px;
  }

  /* Back */
  .services {
    position: absolute; left: 0; right: 0; top: 238px;
    text-align: center; color: var(--text-light);
    font-family: "Caladea", Georgia, serif;
  }
  .services__heading {
    font-family: "Cinzel", "Times New Roman", serif;
    font-weight: 500; font-size: 29px; letter-spacing: 1px;
    margin-bottom: 12px;
  }
  .services__list { list-style: none; font-size: 21px; line-height: 26px; }
  .services__divider { display: block; margin: 10px auto 12px; }
  .skyline--back {
    bottom: 0; height: 150px;
    background: linear-gradient(180deg, rgba(255,255,255,0) 0%, rgba(255,255,255,.7) 45%, var(--paper) 62%, var(--paper) 100%);
  }
</style>
</head>
<body>
<main class="canvas">

  <section class="card card--front" aria-label="Card front">
    <div class="brand">
      <span class="brand__mark"></span>
      <div class="brand__name">Stonebrook<span>Realty Partners of Chicago</span></div>
    </div>
    <div class="skyline skyline--front" role="img" aria-label="Blue Chicago skyline silhouette"></div>
    <div class="front__panel">
      <h1 class="person__name">DEREK OLLANBY</h1>
      <p class="person__title">Director of Acquisitions</p>
      <ul class="contact">
        <li>T: 630-517-2946</li>
        <li>E: Derek@StonebrookRPC.com</li>
        <li>W: www.StonebrookRPC.com</li>
      </ul>
    </div>
  </section>

  <section class="card card--back" aria-label="Card back">
    <div class="services">
      <h2 class="services__heading">WE SPECIALIZE IN</h2>
      <ul class="services__list">
        <li>Buying and Selling<br>Real Estate,</li>
        <li><svg class="services__divider" width="22" height="22" viewBox="0 0 22 22" aria-hidden="true"><circle cx="11" cy="11" r="9.5" fill="none" stroke="#fff" stroke-width="2"/><circle cx="11" cy="11" r="5" fill="none" stroke="#fff" stroke-width="2"/></svg>Property Management,</li>
        <li><svg class="services__divider" width="22" height="22" viewBox="0 0 22 22" aria-hidden="true"><circle cx="11" cy="11" r="9.5" fill="none" stroke="#fff" stroke-width="2"/><circle cx="11" cy="11" r="5" fill="none" stroke="#fff" stroke-width="2"/></svg>Real Estate Investments<br>(Flips &amp; Rentals)</li>
      </ul>
    </div>
    <div class="skyline skyline--back" role="img" aria-label="White Chicago skyline silhouette"></div>
  </section>

</main>
</body>
</html>
```